A Label for an ECO Friendly Spirit Company

Design a label which can be used for vodka and gin (London Dry Gin). It should be Square type Like the Shape File you see in the uploads. VORK means Local Eco friendly Authentic and Fair. We want a cool and slim label that calls for eco-friendly. We want to use it for our premium
Vodka and our London Dry Gin. Please use the logo and design it in Square Type.

40%vol, 700ml

Target Market(s)

spirits and events

Industry/Entity Type

SPIRITS

Colors
00AB8E
00BBA5
67D7C9
C6EFE9
E9F9F6
59FF00
82FF00
B8FF75
E3FFCB
F4FFEA

Requirements
Must have
• Logo from VORK, Squaee Shape

```html
<!DOCTYPE html>
<html lang="en">
<head>
<meta charset="utf-8">
<title>VORK Vodka Label</title>
<link rel="stylesheet" href="https://fonts.googleapis.com/css2?family=Montserrat:wght@400;500&family=Roboto+Condensed:wght@400&family=Great+Vibes&display=swap">
<style>
  :root {
    --page: #f5f6f8;
    --label-teal: #0f6f64;
    --leaf-green: #4fb548;
    --leaf-lime: #b5d334;
    --leaf-olive: #8a7a3a;
    --brand: #1fa88c;
    --brand-square: #9ccf2e;
    --text-light: #ffffff;
    --script-yellow: #e6ef7a;
  }
  * { margin: 0; padding: 0; box-sizing: border-box; }
  html, body {
    width: 1200px;
    height: 1086px;
    overflow: hidden;
    background: var(--page);
  }
  .canvas {
    position: relative;
    width: 1200px;
    height: 1086px;
  }
  .label-shape {
    position: absolute;
    inset: 0;
  }
  .label-text {
    position: absolute;
    left: 0;
    width: 1200px;
    text-align: center;
    color: var(--text-light);
  }
  .brand {
    top: 370px;
    display: flex;
    justify-content: center;
    align-items: center;
    gap: 16px;
  }
  .brand-square {
    width: 34px;
    height: 34px;
    background: var(--brand-square);
  }
  .brand-name {
    font-family: "Montserrat", sans-serif;
    font-weight: 500;
    font-size: 68px;
    letter-spacing: 2px;
    line-height: 1;
    color: var(--brand);
  }
  .product {
    top: 535px;
    font-family: "Montserrat", sans-serif;
    font-weight: 400;
    font-size: 92px;
    letter-spacing: 6px;
    line-height: 1;
  }
  .origin {
    top: 652px;
    font-family: "Roboto Condensed", sans-serif;
    font-size: 16px;
    letter-spacing: 1.5px;
    text-transform: uppercase;
  }
  .edition {
    top: 694px;
    font-family: "Great Vibes", cursive;
    font-size: 44px;
    color: var(--script-yellow);
  }
  .specs {
    top: 783px;
    font-family: "Montserrat", sans-serif;
    font-size: 18px;
    letter-spacing: 1.5px;
  }
</style>
</head>
<body>
  <main class="canvas">
    <svg class="label-shape" width="1200" height="1086" viewBox="0 0 1200 1086">
      <defs>
        <radialGradient id="leaf-border" cx="50%" cy="50%" r="55%">
          <stop offset="0.55" stop-color="#0f6f64" stop-opacity="0"/>
          <stop offset="0.8" stop-color="#4fb548" stop-opacity="0.55"/>
          <stop offset="1" stop-color="#a9c93a" stop-opacity="0.8"/>
        </radialGradient>
      </defs>
      <polygon class="label-base" points="600,93 1050,543 600,993 150,543" fill="var(--label-teal)"/>
      <polygon class="leaf-pattern" role="img" aria-label="Scattered green, lime and olive leaf illustrations around the label edges" points="600,93 1050,543 600,993 150,543" fill="url(#leaf-border)"/>
    </svg>

    <div class="label-text brand">
      <span class="brand-square"></span>
      <span class="brand-name">VORK</span>
    </div>
    <h1 class="label-text product">VODKA</h1>
    <p class="label-text origin">Produced &amp; Bottled in Germany</p>
    <p class="label-text edition">Signature Blend</p>
    <p class="label-text specs">40%vol | 700ml</p>
  </main>
</body>
</html>
```